Business Card Design

I need a business card design for a new company based in Australind, Western Australia. The business is for puppet shows at children's parties, fetes, custom puppet builds, etc.Attached is a picture of Ray Caldwick in silhouette. I was thinking a design of a puppeteer at the top of some stairs talking to a puppet in silhouette but open to suggestions. (Under the willow is named as I do all my puppet builds in the top room of my house (at the Under the willow).

Industry/Entity Type

Business

Contact Information for Business Card

Under The Willow Puppets, Dale Munroe, Puppeteer / Puppet Builder, phone - 0438215076, Puppet shows / Custom Puppet Builds, Working With Children

Requirements
Must have
• Name and Logo on one side. Second side to have business card details.

```html
<!DOCTYPE html>
<html lang="en">
<head>
<meta charset="utf-8">
<title>Under The Willow Puppets – Business Card</title>
<link rel="stylesheet" href="https://fonts.googleapis.com/css2?family=Open+Sans:wght@400;600;700&display=swap">
<style>
  :root {
    --page-bg: #e9e6e1;
    --card-bg: #f7f6f3;
    --title-red: #8e1a1c;
    --ink: #111111;
    --rule: #1a1a1a;
    --photo-dark: #1c2118;
    --photo-mid: #3a4434;
    --photo-light: #c9ccc0;
  }
  * { box-sizing: border-box; margin: 0; padding: 0; }
  html, body {
    width: 1200px;
    height: 857px;
    overflow: hidden;
    background: var(--page-bg);
    font-family: "Open Sans", sans-serif;
  }
  .card {
    position: absolute;
    left: 100px;
    top: 142px;
    width: 1000px;
    height: 572px;
    background: var(--card-bg);
    box-shadow: 0 4px 18px rgba(0,0,0,0.18);
  }
  .card__title {
    position: absolute;
    left: 70px;
    top: 28px;
    font-size: 62px;
    font-weight: 400;
    letter-spacing: 3px;
    color: var(--title-red);
    white-space: nowrap;
  }
  .card__photo {
    position: absolute;
    left: 40px;
    top: 165px;
    width: 430px;
    height: 390px;
    border: 5px solid var(--ink);
    border-radius: 10px;
    background:
      radial-gradient(ellipse at 70% 55%, var(--photo-dark) 0%, var(--photo-dark) 35%, transparent 60%),
      linear-gradient(120deg, var(--photo-light) 0%, #a9ae9f 40%, var(--photo-mid) 75%, var(--photo-dark) 100%);
  }
  .card__rule {
    position: absolute;
    left: 492px;
    top: 110px;
    width: 2px;
    height: 450px;
    background: var(--rule);
  }
  .card__details {
    position: absolute;
    left: 522px;
    top: 118px;
    color: var(--ink);
    font-weight: 600;
  }
  .details__name {
    font-size: 50px;
    font-weight: 600;
    line-height: 1.15;
  }
  .details__role,
  .details__phone {
    font-size: 29px;
    line-height: 1.35;
    letter-spacing: 1px;
  }
  .details__services {
    margin-top: 92px;
    font-size: 29px;
    line-height: 1.3;
    letter-spacing: 1px;
  }
</style>
</head>
<body>
  <div class="card">
    <h1 class="card__title">Under The Willow Puppets</h1>
    <div class="card__photo" role="img" aria-label="Photo of a puppeteer in silhouette sitting by a window, holding a hand puppet"></div>
    <div class="card__rule"></div>
    <div class="card__details">
      <p class="details__name">Dale Munroe</p>
      <p class="details__role">Puppeteer / Puppet Builder</p>
      <p class="details__phone">0438215076</p>
      <div class="details__services">
        <p>2735916</p>
        <p>Puppet shows /</p>
        <p>Custom Puppet Builds,</p>
        <p>Working With Children</p>
      </div>
    </div>
  </div>
</body>
</html>
```